Kestrel Electrical Business Card

We need a business card design for our family-run electrical contracting business based in Western Australia called 'Kestrel Electrical'. We provide electrical services including residential, commercial and industrial. We aim for individual business cards to be made for all of our employees. We already have a company logo, which we require to be featured on the design. We would like simple, sleek and vibrant designs, which incorporate our logo and represent our business. We do not want anything involving too many graphics/images. We like the colours red, black, white and all shades of grey. The final design should communicate professionalism and trustworthiness.
We require the following contact information:
Name- Owen Strickland
EC 5809
Mobile number- 0455 918 302
Fax number (including area code)- (08) 9640 2718
Email adress- name@kestrelelectrical.example
Electrical
- ITC Handel Bold

```html
<!DOCTYPE html>
<html lang="en">
<head>
<meta charset="utf-8">
<title>Kestrel Electrical – Business Card</title>
<link rel="stylesheet" href="https://fonts.googleapis.com/css2?family=Open+Sans:wght@400;600;700&display=swap">
<style>
  :root {
    --page-bg: #e6e6e6;
    --card-white: #ffffff;
    --brand-red: #e31e24;
    --charcoal: #2f2f30;
    --text-dark: #2b2b2b;
    --text-grey: #3c3c3c;
  }
  * { margin: 0; padding: 0; box-sizing: border-box; }
  html, body {
    width: 1200px; height: 800px; overflow: hidden;
    background: var(--page-bg);
    font-family: "Open Sans", Arial, sans-serif;
  }
  .canvas {
    width: 1200px; height: 800px;
    display: flex; align-items: center; justify-content: center;
  }
  .business-card {
    position: relative;
    width: 1050px; height: 600px;
    background: var(--card-white);
    box-shadow: 0 6px 24px rgba(0,0,0,0.12);
    overflow: hidden;
  }
  .swoosh { position: absolute; inset: 0; width: 100%; height: 100%; }
  .swoosh .red-band { fill: var(--brand-red); }
  .swoosh .white-gap { fill: var(--card-white); }
  .swoosh .charcoal-band { fill: var(--charcoal); }

  .brand {
    position: absolute; left: 62px; top: 78px;
    display: flex; align-items: center; gap: 18px;
  }
  .brand-square {
    width: 54px; height: 54px; background: var(--brand-red);
  }
  .brand-name {
    font-size: 44px; font-weight: 700; color: var(--text-dark);
    letter-spacing: 0.5px; line-height: 1;
  }

  .person { position: absolute; left: 62px; top: 330px; }
  .person-name {
    font-size: 34px; font-weight: 700; color: var(--brand-red); line-height: 1.15;
  }
  .person-role {
    font-size: 28px; font-weight: 400; color: var(--text-grey); line-height: 1.2;
  }

  .contact { position: absolute; left: 62px; top: 450px; color: var(--text-grey); }
  .address { font-size: 20px; margin-bottom: 10px; }
  .contact-grid {
    display: grid; grid-template-columns: auto auto; column-gap: 34px; row-gap: 6px;
    font-size: 21px;
  }
  .contact-item { display: flex; align-items: center; gap: 10px; white-space: nowrap; }
  .contact-item svg { width: 18px; height: 18px; fill: var(--brand-red); flex: none; }
</style>
</head>
<body>
<main class="canvas">
  <section class="business-card">
    <svg class="swoosh" viewBox="0 0 1050 600" aria-hidden="true">
      <path class="red-band" d="M870 0 C930 230 840 480 430 600 L1050 600 L1050 0 Z"/>
      <path class="white-gap" d="M870 0 C935 220 885 470 620 600 L1050 600 L1050 0 Z"/>
      <path class="charcoal-band" d="M882 0 C950 220 905 480 655 600 L1050 600 L1050 0 Z"/>
    </svg>

    <header class="brand">
      <span class="brand-square"></span>
      <span class="brand-name">Kestrel Electrical</span>
    </header>

    <div class="person">
      <h1 class="person-name">Owen Strickland</h1>
      <p class="person-role">Consultant</p>
    </div>

    <div class="contact">
      <p class="address">Unit 4, 27 Harbour Quay Road, Bunbury WA</p>
      <div class="contact-grid">
        <span class="contact-item">
          <svg viewBox="0 0 24 24"><path d="M6.6 10.8a15 15 0 0 0 6.6 6.6l2.2-2.2c.3-.3.7-.4 1-.2 1.1.4 2.3.6 3.6.6.6 0 1 .4 1 1V20c0 .6-.4 1-1 1A17 17 0 0 1 3 4c0-.6.4-1 1-1h3.5c.6 0 1 .4 1 1 0 1.3.2 2.5.6 3.6.1.3 0 .7-.2 1z"/></svg>
          0455 918 302
        </span>
        <span class="contact-item">
          <svg viewBox="0 0 24 24"><path d="M2 5h20v14H2z M4 7v.5l8 5 8-5V7l-8 5z" fill-rule="evenodd"/></svg>
          name@kestrelelectrical.example
        </span>
        <span class="contact-item">
          <svg viewBox="0 0 24 24"><path d="M6 2h12v5H6z M3 8h18v10h-3v4H6v-4H3z M8 14v6h8v-6z" fill-rule="evenodd"/></svg>
          (08) 9640 2718
        </span>
        <span class="contact-item">
          <svg viewBox="0 0 24 24"><path d="M12 2a10 10 0 1 0 0 20 10 10 0 0 0 0-20zm0 2c.9 1.2 1.6 2.6 2 4h-4c.4-1.4 1.1-2.8 2-4zM4.3 14a8 8 0 0 1 0-4h3.4a16 16 0 0 0 0 4zm.8 2h3c.3 1.3.8 2.5 1.4 3.6A8 8 0 0 1 5.1 16zm3-8h-3a8 8 0 0 1 4.4-3.6C8.9 5.5 8.4 6.7 8.1 8zM12 20c-.9-1.2-1.6-2.6-2-4h4c-.4 1.4-1.1 2.8-2 4zm2.3-6H9.7a14 14 0 0 1 0-4h4.6a14 14 0 0 1 0 4zm.2 5.6c.6-1.1 1.1-2.3 1.4-3.6h3a8 8 0 0 1-4.4 3.6zm1.8-5.6a16 16 0 0 0 0-4h3.4a8 8 0 0 1 0 4zM15.9 8c-.3-1.3-.8-2.5-1.4-3.6A8 8 0 0 1 18.9 8z"/></svg>
          www.kestrelelectrical.example
        </span>
      </div>
    </div>
  </section>
</main>
</body>
</html>
```